Life and business Coaching Business Card and Logo

A new design for new company. We coach people to get the best out of themselves in business, life, health , family, career, relationships.
we work in Professional, executive, business and corporate environment. We use art and the processes of making art to work with getting people to delve into and change their mind maps or the way they are currently thinking so that they can move forward towards their goals strategically.
Updates

Project Deadline Extended
Reason: I have been laid up in bed with back problems and have just been able to get back to view designs. several are quiet good and I have given feedback today. I also want to take my project off refundable status as I will choose a design from this brief. regards Marisol

Target Market(s)

Professional artistic and bold energetic individuals

Industry/Entity Type

Health

Contact Information for Business Card

Vel5Mentoring, Marisol Drayke, Shaping Days Boldly,
Mob:0419586740, Ph: +61 8 95820647,
Professional, Executive, Business and Corporate Coach

Requirements
Must have
• a logo that can be used on all promotional and stationary material.
Should contain a person and be bold/colourful, simple and artistic.
Nice to have
• Room to place qualifications of Business

```html
<!DOCTYPE html>
<html lang="en">
<head>
<meta charset="utf-8">
<title>Vel5Mentoring Business Card</title>
<link href="https://fonts.googleapis.com/css2?family=Righteous&display=swap" rel="stylesheet">
<style>
  :root {
    --teal: #1aa9a3;
    --teal-deep: #128e89;
    --teal-soft: #bfe6e3;
    --mist: #e9f6f5;
    --paper: #ffffff;
    --backdrop: #eef5f5;
  }
  html, body {
    margin: 0;
    width: 1200px;
    height: 900px;
    overflow: hidden;
    background: var(--backdrop);
  }
  .business-card {
    position: absolute;
    left: 150px;
    top: 200px;
    width: 900px;
    height: 500px;
    border-radius: 22px;
    overflow: hidden;
    font-family: "Righteous", sans-serif;
    color: var(--teal);
    box-shadow: 0 6px 18px rgba(18, 142, 137, 0.18);
  }
  .card-surface {
    position: absolute;
    inset: 0;
    background: linear-gradient(180deg, var(--teal-soft) 0%, var(--mist) 35%, var(--paper) 70%, var(--mist) 88%, var(--teal-soft) 100%);
  }
  .card-shapes {
    position: absolute;
    inset: 0;
  }
  .service-list {
    position: absolute;
    left: 20px;
    top: 68px;
    margin: 0;
    padding: 0;
    list-style: none;
    display: flex;
    gap: 30px;
    color: var(--paper);
    font-size: 17px;
    letter-spacing: 0.5px;
    text-transform: uppercase;
    transform: rotate(-2.6deg);
    transform-origin: left center;
  }
  .service-list li::before {
    content: "";
    display: inline-block;
    width: 10px;
    height: 10px;
    margin-right: 8px;
    background: var(--paper);
    vertical-align: 1px;
  }
  .brand {
    position: absolute;
    left: 0;
    right: 0;
    top: 170px;
    text-align: center;
  }
  .brand-mark {
    display: inline-flex;
    align-items: center;
    gap: 14px;
  }
  .brand-dot {
    width: 34px;
    height: 34px;
    border-radius: 50%;
    background: var(--teal);
  }
  .brand-name {
    margin: 0;
    font-size: 44px;
    font-weight: 400;
    color: var(--teal);
    text-transform: uppercase;
    letter-spacing: 1px;
  }
  .brand-tagline {
    margin: 6px 0 0;
    font-size: 20px;
    color: var(--teal-deep);
    text-transform: uppercase;
    letter-spacing: 1.5px;
  }
  .contact-block {
    position: absolute;
    right: 34px;
    top: 282px;
    text-align: right;
    font-size: 17px;
    line-height: 1.55;
    text-transform: uppercase;
    letter-spacing: 0.8px;
    color: var(--teal);
    font-style: normal;
  }
  .contact-block p { margin: 0; }
</style>
</head>
<body>
  <article class="business-card">
    <div class="card-surface"></div>
    <svg class="card-shapes" width="900" height="500" viewBox="0 0 900 500" aria-hidden="true">
      <path class="top-band" d="M0 62 L820 30 Q860 28 880 0 L900 0 L900 18 Q880 52 840 56 L0 100 Z" fill="var(--teal)"/>
      <path class="bottom-band" d="M260 500 L260 478 Q262 458 300 456 L900 440 L900 500 Z" fill="var(--teal)"/>
    </svg>

    <ul class="service-list">
      <li>Professional</li>
      <li>Executive</li>
      <li>Business</li>
      <li>Corporate Coach</li>
    </ul>

    <header class="brand">
      <div class="brand-mark">
        <span class="brand-dot"></span>
        <h1 class="brand-name">Vel5Mentoring</h1>
      </div>
      <p class="brand-tagline">Shaping Days Boldly</p>
    </header>

    <address class="contact-block">
      <p>Vel5Mentoring</p>
      <p>Marisol Drayke</p>
      <p>Shaping Days Boldly</p>
      <p>Mob:0419586740</p>
      <p>Ph: +61 8 95820647</p>
    </address>
  </article>
</body>
</html>
```